Banking and Finance Website

Our client provides Business-To-Business Financial services.

They are not a bank but do provide transactions to bank and finance institutions.

Require a new design to update and old website. http://www.quarnleygroup.example/

The design should be:

(Please see design mood board of other styles)
Corporate
“Clean” Look
Designed to convey Trust and Authority.

Must incorporate:
Search Option (Top Right) Colours and Branding Matching Site
Telephone Number: Top Left or right Colours and Branding Matching Site
Contact: Clear contact form and or device.
If your design is heavily image based then you avoid this request, otherwise:

TEXT: Quarnley is an independent management owned Tavener's Broking group operating in the Harbourline Market for over 40 years - and prides itself on providing a dynamic service both to Clients and to Underwriters. Its origins date back to the Quarnley family in Italy where they have been involved in the insurance business for. generations. The company also enjoys a minority shareholding by insurance investment specialist, R T Wendle & Partners Plc.

Through its Tavener's broking subsidiary, Quarnley Limited, the specialist divisions are led by experienced executives - further information can be obtained by clicking the relevant links on this page.

Quarnley is primarily dedicated to working with other brokers and intermediaries across the world where they need specialist access to the Tavener's and London / Bermudian insurance & reinsurance markets. The Groups reputation has been built upon its ability to place complex or high risk commercial insurance contracts - many of them now executed under binding authority facilities held by Quarnley Limited.

Our UK department offers the full range of insurance products both via regional insurance intermediaries and to direct clients often with complicated / bespoke placements.

Styles we think convey the correct image:

http://www.velmoracraft.example/
http://www.holtbyguide.example/
https://www.fernvalcapital.example/uk/en/
http://www2.orbisthane.example/
Updates

Please see added logo and brand images. These can be vectored and used abstract as you wish as they are quite dated. 

Target Market(s)

Business To Business. Financiers , International

Industry/Entity Type

Insurance

Requirements
Must have
• Lion/Globe images. ( files attached) might be worth tracing the vectors so you can better incorporate them.

Should not have
• Obvious pictures of money of graphs or stock exchange.

```html
<!DOCTYPE html>
<html lang="en">
<head>
<meta charset="utf-8">
<title>Quarnley Insurance Group</title>
<link href="https://fonts.googleapis.com/css2?family=Arimo:ital,wght@0,400;0,700;1,400&display=swap" rel="stylesheet">
<style>
:root{
  --brand-blue:#0d4a9c;
  --brand-deep:#08337a;
  --nav-blue:#2f5f9f;
  --heading-blue:#2c63ae;
  --accent-green:#5cb53c;
  --accent-green-dark:#3f8f27;
  --text-grey:#7d7d7d;
  --text-dark:#333;
  --rule:#d8d8d8;
  --page-bg:#e9e9e9;
  --footer-bg:#1c1c1c;
  --white:#fff;
}
*{margin:0;padding:0;box-sizing:border-box}
html,body{width:1050px;height:1200px;overflow:hidden}
body{font-family:"Arimo",Arial,sans-serif;background:var(--page-bg);position:relative;color:var(--text-grey)}
.skyline{position:absolute;left:0;top:560px;width:1050px;height:640px;background:linear-gradient(180deg,#e9e9e9 0%,#b9b9b9 30%,#6d6d6d 70%,#2b2b2b 100%)}
.page{position:absolute;left:118px;top:0;width:817px;height:1138px;background:var(--white);box-shadow:0 0 8px rgba(0,0,0,.25);overflow:hidden}
.masthead{position:absolute;left:0;top:0;width:817px;height:93px;background:linear-gradient(180deg,#1c5cb0 0%,var(--brand-blue) 60%,var(--brand-deep) 100%)}
.brand{position:absolute;left:20px;top:14px;display:flex;align-items:center;gap:10px}
.brand-mark{width:54px;height:54px;background:var(--white);border-radius:3px}
.brand-name{color:var(--white);font-size:19px;letter-spacing:.5px;font-variant:small-caps}
.search{position:absolute;left:603px;top:26px;width:188px;height:20px;background:var(--white);border-radius:10px;border:1px solid #aab}
.search span{position:absolute;left:12px;top:3px;font-size:10px;color:#aaa}
.search svg{position:absolute;right:6px;top:3px}
.contacts{position:absolute;right:26px;top:59px;display:flex;gap:16px;color:var(--white);font-size:12px;font-weight:700;white-space:nowrap}
.contacts div{display:flex;align-items:center;gap:6px}
.nav{position:absolute;left:0;top:93px;width:817px;height:35px;background:linear-gradient(180deg,#4d79b4,var(--nav-blue));display:flex;align-items:center;padding-left:25px}
.nav a{color:var(--white);font-size:11px;text-decoration:none;padding:5px 12px;margin-right:8px;white-space:nowrap}
.nav a.active{background:var(--accent-green);border:1px solid #8fd46f}
.hero-map{position:absolute;left:140px;top:160px;width:430px;height:260px;background:radial-gradient(ellipse at center,#e3f2e0 0%,#f4faf3 60%,#fff 100%)}
.hero-title{position:absolute;left:48px;top:182px;width:470px;font-size:33px;line-height:36px;color:var(--heading-blue);font-weight:400}
.hero-text{position:absolute;left:48px;top:300px;width:440px;font-size:12px;line-height:16px;color:var(--text-grey)}
.cta{position:absolute;left:48px;top:366px;width:199px;height:44px;border-radius:4px;background:linear-gradient(180deg,#7ccb55,var(--accent-green-dark));color:var(--white);font-weight:700;font-size:15px;display:flex;align-items:center;padding-left:14px;white-space:nowrap}
.cta i{position:absolute;right:12px;top:12px;width:20px;height:20px;border-radius:50%;background:#2d6e1a;display:flex;align-items:center;justify-content:center}
.hero-portrait{position:absolute;left:540px;top:150px;width:250px;height:326px;background:linear-gradient(180deg,#f2ece6 0%,#b9a999 45%,#6c6a6c 100%)}
.clients{position:absolute;left:20px;top:478px;width:777px;height:110px;border-top:1px solid var(--rule);border-bottom:3px double var(--rule)}
.clients-label{position:absolute;left:0;right:0;top:2px;text-align:center;font-size:11px;color:var(--heading-blue);letter-spacing:.5px;white-space:nowrap}
.clients-label::before,.clients-label::after{content:"";display:inline-block;width:290px;height:1px;background:var(--rule);vertical-align:middle;margin:0 10px}
.client-row{position:absolute;left:40px;top:38px;width:697px;height:40px;display:flex;justify-content:space-around;align-items:center}
.client-row span{font-size:15px;color:#8c8c8c;display:flex;align-items:center;gap:6px;white-space:nowrap}
.client-row b{width:12px;height:12px;background:#a8a8a8;display:inline-block}
.arrow{position:absolute;top:48px;width:20px;height:20px;border-radius:50%;background:#9a9a9a;display:flex;align-items:center;justify-content:center}
.welcome-title{position:absolute;left:23px;top:622px;font-size:24px;color:var(--heading-blue);font-weight:400}
.welcome-body{position:absolute;left:23px;top:660px;width:500px;font-size:10px;line-height:13.5px;color:var(--text-grey)}
.welcome-body p{margin-bottom:13px}
.director{position:absolute;left:542px;top:627px;width:250px;height:240px;border:1px solid var(--rule);padding:3px}
.director-photo{width:242px;height:145px;background:linear-gradient(160deg,#4a4c50 0%,#2c2d31 60%,#18191c 100%);position:relative}
.director-photo span{position:absolute;right:12px;bottom:8px;color:var(--white);font-size:20px}
.director h4{font-size:13px;font-weight:400;color:var(--text-dark);margin:8px 6px 4px}
.director p{font-size:9px;line-height:12px;margin:0 6px}
.panel{position:absolute;top:905px;height:213px;background:var(--white);border-top:4px solid var(--brand-deep);box-shadow:0 1px 3px rgba(0,0,0,.1)}
.panel.green{border-top-color:var(--accent-green)}
.panel h3{font-size:15px;font-weight:400;color:var(--heading-blue);padding:13px 15px 10px;border-bottom:1px solid var(--rule)}
.panel.contact{left:23px;width:227px}
.panel.resources{left:272px;width:255px}
.panel.testimonials{left:551px;width:241px}
.ct{font-size:9.5px;color:var(--text-dark);padding:0 15px}
.ct .row{display:flex;margin-top:8px}
.ct .lbl{width:50px;flex:none;font-weight:700}
.ct a{color:var(--accent-green);text-decoration:underline;white-space:nowrap}
.ct em{color:var(--text-grey);white-space:nowrap;font-size:9px}
.office{display:flex;gap:8px;margin-top:6px}
.office div{font-size:8px;line-height:10px;color:var(--text-grey)}
.office strong{font-style:italic;font-weight:400;color:var(--text-dark);font-size:9px}
.res-list{list-style:none;padding:6px 15px 0}
.res-list li{font-size:9.5px;color:var(--text-dark);padding:6px 0 6px 10px;border-bottom:1px solid var(--rule);position:relative;white-space:nowrap}
.res-list li::before{content:"›";position:absolute;left:0;top:4px;font-size:11px}
.quote{padding:8px 15px 0;font-size:9.5px}
.quote strong{color:var(--text-dark)}
.quote .role{font-style:italic;color:#999;padding-bottom:5px;border-bottom:1px solid var(--rule);margin-bottom:6px}
.quote p{font-style:italic;color:var(--text-dark);line-height:12px;font-size:9px}
.pill{position:absolute;bottom:8px;width:78px;height:19px;border-radius:4px;background:var(--brand-deep);color:var(--white);font-size:9.5px;display:flex;align-items:center;justify-content:center;gap:6px}
.footer{position:absolute;left:0;top:1138px;width:1050px;height:62px;background:var(--footer-bg);text-align:center;color:var(--white);font-size:10px;padding-top:13px;line-height:16px}
.footer a{color:var(--white);text-decoration:none;margin:0 3px}
</style>
</head>
<body>
<div class="skyline" role="img" aria-label="Greyscale city skyline along the river"></div>

<div class="page">
  <header class="masthead">
    <div class="brand">
      <div class="brand-mark"></div>
      <div class="brand-name">Quarnley Insurance Group</div>
    </div>
    <div class="search"><span>Search</span>
      <svg width="12" height="12" viewBox="0 0 12 12"><circle cx="5" cy="5" r="3.5" fill="none" stroke="#777" stroke-width="1.4"/><line x1="7.6" y1="7.6" x2="11" y2="11" stroke="#777" stroke-width="1.6"/></svg>
    </div>
    <div class="contacts">
      <div><svg width="13" height="11" viewBox="0 0 13 11"><path d="M1 3c0-2 11-2 11 0v1H9V3H4v1H1z M3 5h7l2 5H1z" fill="#fff"/></svg>44 (0) 20 7946 0321</div>
      <div><svg width="14" height="11" viewBox="0 0 14 11"><rect x="0.5" y="0.5" width="13" height="10" rx="1" fill="none" stroke="#fff"/><rect x="2.5" y="3" width="3" height="4" fill="#fff"/><line x1="7" y1="4" x2="12" y2="4" stroke="#fff"/><line x1="7" y1="6.5" x2="12" y2="6.5" stroke="#fff"/></svg>contacts@quarnley.example</div>
    </div>
  </header>

  <nav class="nav">
    <a class="active" href="#">HOME</a><a href="#">ABOUT US</a><a href="#">WHAT WE DO</a><a href="#">LEADER RESOURCES</a><a href="#">OPPORTUNITIES</a><a href="#">NEWS &amp; UPDATES</a><a href="#">CONTACT US</a>
  </nav>

  <div class="hero-map" role="img" aria-label="Faint green world map behind the headline"></div>
  <h1 class="hero-title">Quarnley is an Independent Management Owned Tavener's Broking Group</h1>
  <p class="hero-text">Quarnley is an independent management owned Tavener's Broking group operating in the Harbourline Market for over 40 years - and prides itself on providing a dynamic service both to Clients and to Underwriters.</p>
  <div class="cta">GET STARTED NOW<i><svg width="8" height="9" viewBox="0 0 8 9"><path d="M2 1l4 3.5L2 8" fill="none" stroke="#fff" stroke-width="1.6"/></svg></i></div>
  <div class="hero-portrait" role="img" aria-label="Businesswoman in a grey suit standing with arms folded"></div>

  <section class="clients">
    <div class="clients-label">OUR CLIENTS</div>
    <div class="arrow" style="left:0"><svg width="7" height="9" viewBox="0 0 7 9"><path d="M5 1L2 4.5 5 8" fill="none" stroke="#fff" stroke-width="1.6"/></svg></div>
    <div class="client-row">
      <span><b></b>Corvance</span><span>Meridel Health</span><span>Altoria</span><span>Voltrane</span><span>Kestrel Institute</span><span><b></b>Northvale Institute</span>
    </div>
    <div class="arrow" style="right:0"><svg width="7" height="9" viewBox="0 0 7 9"><path d="M2 1l3 3.5L2 8" fill="none" stroke="#fff" stroke-width="1.6"/></svg></div>
  </section>

  <h2 class="welcome-title">Welcome to The Quarnley Website</h2>
  <div class="welcome-body">
    <p>Quarnley is an independent management owned Tavener's Broking group operating in the Harbourline Market for over 40 years - and prides itself on providing a dynamic service both to Clients and to Underwriters. Its origins date back to the Quarnley family in Italy where they have been involved in the insurance business for. generations. The company also enjoys a minority shareholding by insurance investment specialist, R T Wendle &amp; Partners Plc.</p>
    <p>Through its Tavener's broking subsidiary, Quarnley Limited, the specialist divisions are led by experienced executives - further information can be obtained by clicking the relevant links on this page.</p>
    <p>Quarnley is primarily dedicated to working with other brokers and intermediaries across the world where they need specialist access to the Tavener's and London / Bermudian insurance &amp; reinsurance markets. The Groups reputation has been built upon its ability to place complex or high risk commercial insurance contracts - many of them now executed under binding authority facilities held by Quarnley Limited.</p>
    <p>Our UK department offers the full range of insurance products both via regional insurance intermediaries and to direct clients often with complicated / bespoke placements.</p>
  </div>

  <aside class="director">
    <div class="director-photo" role="img" aria-label="Portrait of the managing director"><span>Mei Lanford</span></div>
    <h4>Managing Director</h4>
    <p>Lorem Ipsum is simply dummy text of the printing and type-setting industry. Lorem Ipsum has been the industry's standard dummy text ever since the 1500s, when an unknown printer.</p>
  </aside>

  <section class="panel contact">
    <h3>Contact Details</h3>
    <div class="ct">
      <div class="row"><span class="lbl">Email</span><span><a href="#">mail@quarnleyoffice.example</a><br><em>Owen Pellard, Managing Director</em></span></div>
      <div class="row"><span class="lbl">Phone:</span><span>44 (0) 20 7946 0321</span></div>
      <div class="row"><span class="lbl">Location</span></div>
      <div class="office">
        <svg width="40" height="38" viewBox="0 0 40 38"><rect x="2" y="14" width="36" height="22" fill="#8cc46b"/><path d="M2 26l12-8 10 10 14-9" fill="none" stroke="#5d9ad6" stroke-width="3"/><path d="M20 2a8 8 0 0 1 8 8c0 6-8 14-8 14s-8-8-8-14a8 8 0 0 1 8-8z" fill="#e8562a"/><circle cx="20" cy="10" r="3" fill="#fff"/></svg>
        <div><strong>Corporate Office</strong><br>Quarnley Insurance Group<br>Limited, 14-16 Ashgrove Row,<br>London, EC1Z 9QX</div>
      </div>
    </div>
  </section>

  <section class="panel green resources">
    <h3>Quarnley Resources</h3>
    <ul class="res-list">
      <li>Talent Management in Emerging Markets</li>
      <li>Attracting Talent in China</li>
      <li>Supporting Business Growth Podcast</li>
      <li>10 Solutions For Email</li>
    </ul>
    <div class="pill" style="left:11px">Read more <svg width="5" height="7" viewBox="0 0 5 7"><path d="M1 1l3 2.5L1 6" fill="none" stroke="#fff"/></svg></div>
  </section>

  <section class="panel testimonials">
    <h3>Clints Testimonials</h3>
    <div class="quote">
      <strong>Carys Denholm</strong>
      <div class="role">National Manager - northvale.example</div>
      <p>NIHS – Northvale Institute for Health Studies is associate with Brightfold Solutions from the day NIHS was born in 2004, today we stand tall as the world largest Institute for Clinical Research and Healthcare. www.northvale.example who have played a vital...</p>
    </div>
    <div class="pill" style="left:15px">View all <svg width="5" height="7" viewBox="0 0 5 7"><path d="M1 1l3 2.5L1 6" fill="none" stroke="#fff"/></svg></div>
  </section>
</div>

<footer class="footer">
  <a href="#">Home</a>| <a href="#">About us</a>| <a href="#">What we do</a>| <a href="#">Leader Resources</a>| <a href="#">Opportunities</a>| <a href="#">News &amp; Updates</a>| <a href="#">Contact us</a><br>
  Copyright © Quarnley Insurance Group Limited 2011
</footer>
</body>
</html>
```